A4 Flyer

Brightwell Care Academy is starting a course in regional Victoria. We are currently advertising (See attached file A34984) in local papers but need to create a one page flyer to distribute to Aged Care facilities in the area. The A4 flyer will be inserted into a folder pack with more detailed information on Brightwell Care Academy. Important to use images and logoes attached

Target Market(s)

Flyer to be distributed to Aged Care facility staff and owners

Industry/Entity Type

Advertising

Font styles to use
Sans Serif

Colors
f37123
ec1f27

Requirements
Must have
• BCA Logo
Some image

```html
<!DOCTYPE html>
<html lang="en">
<head>
<meta charset="utf-8">
<title>Brightwell Care Academy – A4 Flyer</title>
<link rel="stylesheet" href="https://fonts.googleapis.com/css2?family=Montserrat:wght@700;800&family=Open+Sans:wght@400;600&family=Roboto+Condensed:wght@400&display=swap">
<style>
  :root {
    --orange: #f37123;
    --red: #ec1f27;
    --deep-orange: #ef5a24;
    --ink: #4a4a4a;
    --white: #ffffff;
    --backdrop: #d9d9d9;
    --photo-warm: #e9ddd6;
    --photo-dark: #2b2a2c;
  }
  * { margin: 0; padding: 0; box-sizing: border-box; }
  html, body { width: 1200px; height: 1000px; overflow: hidden; }
  body { background: var(--backdrop); position: relative; font-family: "Open Sans", sans-serif; }

  .flyer {
    position: absolute; left: 300px; top: 76px;
    width: 600px; height: 848px;
    background: var(--white);
    overflow: hidden;
  }
  .flyer > * { position: absolute; }

  .header-band, .footer-band { left: 0; width: 600px; }
  .header-band { top: 0; height: 150px; }
  .footer-band { bottom: 0; height: 140px; }

  .headline {
    top: 34px; left: 0; width: 600px; text-align: center;
    font-family: "Montserrat", sans-serif; font-weight: 800;
    font-size: 31px; letter-spacing: 1px; color: var(--white);
  }
  .subline {
    top: 74px; left: 0; width: 600px; text-align: center; padding-left: 10px;
    font-family: "Roboto Condensed", sans-serif; font-size: 21px; color: var(--white);
  }

  .hero-photo {
    left: 0; top: 110px; width: 380px; height: 490px;
    background:
      linear-gradient(90deg, rgba(255,255,255,0) 55%, var(--white) 100%),
      linear-gradient(180deg, rgba(255,255,255,0) 70%, var(--white) 100%),
      radial-gradient(ellipse at 35% 45%, var(--photo-dark) 0%, #5a4c48 35%, var(--photo-warm) 70%);
  }

  .qualification {
    top: 170px; right: 45px; text-align: right; white-space: nowrap;
    font-family: "Roboto Condensed", sans-serif; font-size: 18px; line-height: 28px;
    color: var(--deep-orange); text-transform: uppercase;
  }
  .funding {
    top: 242px; left: 306px;
    font-family: "Open Sans", sans-serif; font-size: 21px; line-height: 30px; color: var(--ink);
  }
  .funding .price {
    font-family: "Montserrat", sans-serif; font-weight: 700; font-size: 36px; color: var(--deep-orange);
  }

  .photo-frame { border: 2px solid var(--orange); }
  .photo-frame--desk {
    left: 257px; top: 416px; width: 145px; height: 167px;
    background: linear-gradient(160deg, #f4f4f4 0%, #d8d2cc 55%, #efefef 100%);
  }
  .photo-frame--anatomy {
    left: 408px; top: 383px; width: 147px; height: 168px;
    background: linear-gradient(160deg, #f5f5f5 0%, #e6cfc4 50%, #f1f1f1 100%);
  }

  .brand {
    left: 42px; top: 612px; width: 200px; height: 70px;
    display: flex; align-items: center; gap: 10px;
  }
  .brand-dot { width: 44px; height: 44px; border-radius: 50%; background: var(--orange); flex: none; }
  .brand-name {
    font-family: "Open Sans", sans-serif; font-weight: 600; font-size: 17px; line-height: 20px;
    color: var(--ink);
  }

  .course-list {
    left: 255px; top: 602px; height: 90px; width: 320px;
    border-left: 2px solid var(--ink); padding-left: 11px;
    list-style: none; display: flex; flex-wrap: wrap; align-content: space-between; column-gap: 8px;
    font-size: 15.5px; line-height: 21px; color: var(--ink);
  }
  .course-list li { display: flex; align-items: center; white-space: nowrap; }
  .course-list li::before {
    content: ""; width: 10px; height: 10px; border-radius: 50%;
    background: var(--deep-orange); margin-right: 4px;
  }
  .course-list .row-break { flex-basis: 100%; height: 0; }

  .enrol {
    left: 88px; top: 752px;
    display: grid; grid-template-columns: auto auto; column-gap: 14px;
    font-family: "Open Sans", sans-serif; font-size: 19px; line-height: 22px; color: var(--white);
  }
  .enrol dt { text-align: right; text-transform: uppercase; }
  .disclaimer {
    left: 0; top: 806px; width: 600px; text-align: center;
    font-size: 13.5px; font-weight: 600; color: var(--white);
  }
</style>
</head>
<body>
  <article class="flyer">
    <div class="hero-photo" role="img" aria-label="Photo of a smiling student seated at a desk in a training room"></div>

    <svg class="header-band" viewBox="0 0 600 150" aria-hidden="true">
      <defs>
        <linearGradient id="band-top" x1="0" y1="0" x2="1" y2="0">
          <stop offset="0" stop-color="#f58a2a"/>
          <stop offset="1" stop-color="#ee5523"/>
        </linearGradient>
      </defs>
      <path d="M0 0H600V100C430 96 220 100 0 146Z" fill="url(#band-top)"/>
      <path d="M0 146C220 100 430 96 600 100V108C430 104 220 108 0 150Z" fill="#f37123"/>
    </svg>

    <h1 class="headline">UNIQUE OPPORTUNITY!</h1>
    <p class="subline">Fast Track Course - Start July 2014</p>

    <p class="qualification">Double Qualification - Cert III in Aged Care<br>with Home and Community Care</p>
    <p class="funding">Government Funding for<br>Eligible Etudents!<br>Fees from <span class="price">$117</span></p>

    <div class="photo-frame photo-frame--desk" role="img" aria-label="Photo of a student in a white shirt reading papers at a desk"></div>
    <div class="photo-frame photo-frame--anatomy" role="img" aria-label="Photo of a trainer studying an anatomical torso model"></div>

    <div class="brand">
      <span class="brand-dot"></span>
      <span class="brand-name">Brightwell Care<br>Academy</span>
    </div>

    <ul class="course-list">
      <li>Pathology</li><li>Aged Care</li><li>First Aid</li>
      <span class="row-break"></span>
      <li>CPR</li><li>Anaphylaxis</li><li>Health Services</li>
      <span class="row-break"></span>
      <li>Home &amp; Community Care</li>
      <span class="row-break"></span>
      <li>Medications for PCA’s</li>
    </ul>

    <svg class="footer-band" viewBox="0 0 600 140" aria-hidden="true">
      <defs>
        <linearGradient id="band-bottom" x1="0" y1="0" x2="1" y2="0">
          <stop offset="0" stop-color="#f58a2a"/>
          <stop offset="1" stop-color="#ee5523"/>
        </linearGradient>
      </defs>
      <path d="M0 0C200 40 420 44 600 20V140H0Z" fill="#ec4f24"/>
      <path d="M0 8C200 48 420 52 600 28V140H0Z" fill="url(#band-bottom)"/>
    </svg>

    <dl class="enrol">
      <dt>To enrol visit:</dt><dd>brightwellcare.com.au</dd>
      <dt>Call:</dt><dd>9555 0142</dd>
    </dl>
    <p class="disclaimer">This training is delivered with VIC and Comm Govt Funding to eligible students</p>
  </article>
</body>
</html>
```